Craft oriented film company needs a Business Card design

Hi all,
We're a 2-man band film company in New Zealand called Kestrel Pictures. We're good honest blokes, who are very passionate about the craft of film making. I've attached our current logo which has a bit of a crafty/artisan feel that we like. Feel free to use it - or throw the baby out with the bathwater and start again..... you never know, you might inspire a complete brand re-work.

In any case, the vibe we want to give out is that we are solid, dependable and no bullshit - but without compromising creative excellence and being in the now. We like the 'Brooklyn' artisan style of work.

Preferably single sided.

We need the standard stuff:
Name, job title, cellphone, email address and physical address (this can be smaller if you like - street, suburb, city & zip, country [if you want])

Check out our website to learn more about us: kestrelpictures.example

Target Market(s)

Brand marketers and advertising agency creatives looking for video production.

Industry/Entity Type

Baby

Requirements
Should not have
• Nothing flashy or too 'futuristic', we want it to feel grounded and real. A limited colour palette is preferred.
We don't want any film reels or cameras or anything obvious like that.

```html
<!DOCTYPE html>
<html lang="en">
<head>
<meta charset="utf-8">
<title>Kestrel Pictures — Business Card</title>
<link href="https://fonts.googleapis.com/css2?family=Bebas+Neue&display=swap" rel="stylesheet">
<style>
  :root {
    --backdrop: #3a3a3a;
    --card: #ffffff;
    --arc: #e6e5e6;
    --ink: #1c1c1c;
    --icon-fill: #d2d2d2;
    --pattern: #f1f1f1;
  }
  * { box-sizing: border-box; margin: 0; padding: 0; }
  html, body { width: 1200px; height: 800px; overflow: hidden; }
  body {
    background: var(--backdrop);
    position: relative;
    font-family: "Bebas Neue", "Oswald", sans-serif;
    color: var(--ink);
  }
  .card {
    position: absolute;
    left: 312px;
    width: 574px;
    height: 311px;
    background: var(--card);
    border-radius: 10px;
    overflow: hidden;
  }
  .card--front { top: 45px; }
  .card--back { top: 444px; }

  .front__arc {
    position: absolute;
    left: 281px;
    top: -94px;
    width: 498px;
    height: 498px;
    border-radius: 50%;
    background: var(--arc);
  }

  .wordmark {
    position: absolute;
    display: flex;
    align-items: center;
    gap: 14px;
    transform: translate(-50%, -50%);
  }
  .wordmark__dot {
    width: 22px;
    height: 22px;
    border-radius: 50%;
    background: var(--ink);
    flex: none;
  }
  .wordmark__name {
    font-size: 46px;
    line-height: 0.9;
    letter-spacing: 1px;
    color: var(--ink);
  }
  .card--front .wordmark { left: 138px; top: 153px; }
  .card--back .wordmark { left: 288px; top: 154px; }

  .identity {
    position: absolute;
    right: 75px;
    top: 56px;
    text-align: right;
  }
  .identity__name { font-size: 27px; letter-spacing: 1.5px; line-height: 1; }
  .identity__role { font-size: 16px; letter-spacing: 1px; line-height: 1.2; margin-top: 1px; }

  .contact {
    position: absolute;
    right: 53px;
    top: 147px;
    list-style: none;
    text-align: right;
    font-size: 12.5px;
    letter-spacing: 0.8px;
  }
  .contact__item {
    display: flex;
    justify-content: flex-end;
    align-items: flex-start;
    gap: 8px;
    margin-bottom: 9px;
  }
  .contact__text { line-height: 16.5px; }
  .contact__icon { width: 14px; height: 14px; flex: none; margin-top: 1px; }

  .back__pattern {
    position: absolute;
    left: 22px;
    top: 26px;
    width: 530px;
    height: 252px;
    background: var(--pattern);
  }
  .back__site {
    position: absolute;
    left: 0;
    right: 0;
    bottom: 12px;
    text-align: center;
    font-size: 11px;
    letter-spacing: 0.8px;
  }
</style>
</head>
<body>
  <section class="card card--front" aria-label="Business card front">
    <div class="front__arc"></div>

    <div class="wordmark">
      <span class="wordmark__dot"></span>
      <span class="wordmark__name">Kestrel<br>Pictures</span>
    </div>

    <div class="identity">
      <p class="identity__name">Rowan Hartley</p>
      <p class="identity__role">Manager</p>
    </div>

    <ul class="contact">
      <li class="contact__item">
        <span class="contact__text">0219876543</span>
        <svg class="contact__icon" viewBox="0 0 14 14" aria-hidden="true">
          <circle cx="7" cy="7" r="6.3" fill="var(--icon-fill)" stroke="#9a9a9a" stroke-width="0.8"/>
          <rect x="4.8" y="3.6" width="4.4" height="6.8" rx="0.8" fill="var(--ink)"/>
        </svg>
      </li>
      <li class="contact__item">
        <span class="contact__text">info@kestrelpictures.example</span>
        <svg class="contact__icon" viewBox="0 0 14 14" aria-hidden="true">
          <circle cx="7" cy="7" r="6.3" fill="var(--icon-fill)" stroke="#9a9a9a" stroke-width="0.8"/>
          <rect x="3.8" y="4.6" width="6.4" height="4.8" fill="none" stroke="var(--ink)" stroke-width="1"/>
          <path d="M3.8 4.6 L7 7.4 L10.2 4.6" fill="none" stroke="var(--ink)" stroke-width="1"/>
        </svg>
      </li>
      <li class="contact__item">
        <span class="contact__text">#4812BB<br>Harbour Lane<br>Ponsonby Auckland<br>NZ 1011</span>
        <svg class="contact__icon" viewBox="0 0 14 14" aria-hidden="true">
          <circle cx="7" cy="7" r="6.3" fill="var(--icon-fill)" stroke="#9a9a9a" stroke-width="0.8"/>
          <path d="M3.6 7.2 L7 4 L10.4 7.2 M4.8 6.4 V10 H9.2 V6.4" fill="none" stroke="var(--ink)" stroke-width="1"/>
        </svg>
      </li>
    </ul>
  </section>

  <section class="card card--back" aria-label="Business card back">
    <div class="back__pattern" role="img" aria-label="Faint repeating brand pattern across the card background"></div>
    <div class="wordmark">
      <span class="wordmark__dot"></span>
      <span class="wordmark__name">Kestrel<br>Pictures</span>
    </div>
    <p class="back__site">www.kestrelpictures.example</p>
  </section>
</body>
</html>
```